Business Card Design Project

we need a business card design for our company: www.plomvik.ch
It's important to include our already existing logo (see website)

```html
<!DOCTYPE html>
<html lang="en">
<head>
<meta charset="utf-8">
<title>Plomvik – Business Card</title>
<link rel="stylesheet" href="https://fonts.googleapis.com/css2?family=Arimo:wght@400;700&display=swap">
<style>
  :root{
    --bg:#e6e7e9;
    --card-dark:#2a2a2a;
    --brand-blue:#0a6cb8;
    --brand-deep:#0d5fae;
    --brand-sky:#3f8fdd;
    --logo-blue:#2f7fd0;
    --logo-light:#7fb0e6;
    --band-white:#ffffff;
    --band-shade:#e9ebee;
    --text-light:#ffffff;
  }
  *{margin:0;padding:0;box-sizing:border-box}
  html,body{width:1200px;height:900px;overflow:hidden}
  body{background:var(--bg);font-family:"Arimo",Arial,sans-serif;position:relative}

  .card{position:absolute;box-shadow:0 6px 16px rgba(0,0,0,.35)}

  /* front side */
  .card-front{left:490px;top:110px;width:590px;height:350px;overflow:hidden}
  .front-backdrop{position:absolute;inset:0;
    background:radial-gradient(ellipse at 70% 85%,#5cc0f0 0%,rgba(92,192,240,0) 45%),
               radial-gradient(ellipse at 60% 10%,#4a9ae4 0%,rgba(74,154,228,0) 50%),
               linear-gradient(135deg,var(--brand-deep) 0%,var(--brand-sky) 55%,var(--brand-deep) 100%)}
  .front-band{position:absolute;left:0;right:0;top:100px;height:150px;
    background:linear-gradient(180deg,var(--band-white) 0%,var(--band-shade) 100%);
    display:flex;align-items:center;justify-content:center}
  .front-wordmark{font-weight:700;font-size:82px;color:var(--logo-blue);letter-spacing:-1px}

  /* back side */
  .card-back{left:115px;top:440px;width:600px;height:355px;background:var(--card-dark)}
  .back-wordmark{position:absolute;left:58px;top:132px;font-weight:700;font-size:44px;color:var(--logo-light);letter-spacing:-.5px}
  .back-url{position:absolute;left:62px;top:196px;font-size:17px;color:var(--text-light)}

  .info-block{position:absolute;left:308px;right:8px;background:var(--brand-blue);
    color:var(--text-light);box-shadow:0 3px 6px rgba(0,0,0,.45);padding:0 22px}
  .info-name{top:30px;height:70px;padding-top:12px}
  .person-name{font-weight:700;font-size:21px;line-height:1.2}
  .person-role{font-size:16px;line-height:1.3}
  .info-address{top:128px;height:70px;padding-top:15px;font-size:17px;line-height:1.3}
  .info-contact{top:226px;height:76px;padding-top:8px;font-size:17px;line-height:1.28}
  .contact-line{display:flex;align-items:center;gap:10px}
  .contact-line svg{width:13px;height:13px;flex:none}
</style>
</head>
<body>

  <section class="card card-front" aria-label="Card front">
    <div class="front-backdrop" role="img" aria-label="Blue background with soft light swooshes"></div>
    <div class="front-band">
      <span class="front-wordmark">Plomvik</span>
    </div>
  </section>

  <section class="card card-back" aria-label="Card back">
    <span class="back-wordmark">Plomvik</span>
    <span class="back-url">www.plomvik.ch</span>

    <div class="info-block info-name">
      <div class="person-name">Lena Marti</div>
      <div class="person-role">Co-Founder</div>
    </div>

    <div class="info-block info-address">
      <div>Talackerweg 17</div>
      <div>8052 Zürich</div>
    </div>

    <div class="info-block info-contact">
      <div class="contact-line">
        <svg viewBox="0 0 16 16" aria-hidden="true"><path fill="#cfe3f7" d="M3.5 1.5l2.5 2.5-1.5 2a9 9 0 0 0 5.5 5.5l2-1.5 2.5 2.5-2 2C6 15 1 10 1.5 3.5z"/></svg>
        <span>+41 44 000 18 36</span>
      </div>
      <div class="contact-line">
        <svg viewBox="0 0 16 16" aria-hidden="true"><rect x="1" y="3" width="14" height="10" fill="#cfe3f7"/><path d="M1 3l7 6 7-6" fill="none" stroke="#0a6cb8" stroke-width="1.4"/></svg>
        <span>info@plomvik.ch</span>
      </div>
      <div class="contact-line">
        <svg viewBox="0 0 16 16" aria-hidden="true"><circle cx="8" cy="8" r="7" fill="#cfe3f7"/></svg>
        <span>plomvik.ch</span>
      </div>
    </div>
  </section>

</body>
</html>
```